Business Card Design for Varnel

I've already got the logo, but I'd like to see some interesting designs.

I don't want anything to complex. I like it simple,yet innovative, like the logo.

My business is System Administration for small to medium size businesses, so that will be my main target audience.
Updates

hey all, the png has been uploaded.

Hey all,

If you are submitting the back side of the card, I'd like the top bit of the card to be Varnel Solutions and the logo, the bottom of the card the website, with a white background.

The middle I'd like to leave blank for a quote that will be printed on each card.

Thanks!

Doug

Industry/Entity Type

Business

```html
<!DOCTYPE html>
<html lang="en">
<head>
<meta charset="utf-8">
<title>Varnel Solutions – Business Card</title>
<link href="https://fonts.googleapis.com/css2?family=Lato:wght@400;700&display=swap" rel="stylesheet">
<style>
  :root {
    --brand-blue: #2a7ab8;
    --ink: #333a40;
    --card-white: #ffffff;
    --backdrop: #dfe5e8;
  }
  * { margin: 0; padding: 0; box-sizing: border-box; }
  html, body {
    width: 1200px; height: 960px; overflow: hidden;
    background: var(--backdrop);
    font-family: 'Lato', sans-serif;
  }
  .sheet {
    width: 1200px; height: 960px;
    display: flex; flex-direction: column; align-items: center; justify-content: center;
    gap: 60px;
  }
  .card {
    position: relative;
    width: 700px; height: 400px;
    background: var(--card-white);
    box-shadow: 0 6px 20px rgba(40, 60, 70, 0.18);
  }
  .brand {
    display: flex; align-items: center; gap: 16px;
    color: var(--brand-blue);
    font-weight: 700;
    white-space: nowrap;
  }
  .brand-dot { border-radius: 50%; background: var(--brand-blue); flex: none; }

  /* Front */
  .card-front .brand {
    position: absolute; top: 52px; left: 0; right: 0; justify-content: center;
    font-size: 36px;
  }
  .card-front .brand-dot { width: 58px; height: 58px; }
  .person {
    position: absolute; top: 180px; left: 0; right: 0; text-align: center; color: var(--ink);
  }
  .person-name { font-size: 27px; font-weight: 400; letter-spacing: 0.5px; }
  .person-role { font-size: 16px; margin-top: 4px; }
  .contact { margin-top: 16px; font-size: 17px; line-height: 1.45; }
  .contact .label, .contact .sep, .contact .web { color: var(--brand-blue); }
  .address-band {
    position: absolute; left: 0; right: 0; top: 318px; height: 46px;
    background: var(--brand-blue);
    color: var(--card-white);
    font-size: 19px;
    display: flex; align-items: center; justify-content: center;
  }

  /* Back */
  .card-back .brand {
    position: absolute; top: 40px; right: 36px;
    font-size: 28px; gap: 12px;
  }
  .card-back .brand-dot { width: 40px; height: 40px; }
  .back-web {
    position: absolute; right: 36px; bottom: 24px;
    color: var(--brand-blue); font-size: 17px;
  }
  .back-edge {
    position: absolute; right: 0; bottom: 18px; width: 12px; height: 32px;
    background: var(--brand-blue);
  }
</style>
</head>
<body>
<main class="sheet">
  <section class="card card-front">
    <div class="brand"><span class="brand-dot"></span><span class="brand-name">Varnel Solutions</span></div>
    <div class="person">
      <h1 class="person-name">DANA WHITFIELD</h1>
      <p class="person-role">Operation Manager</p>
      <p class="contact">
        <span class="label">T</span>: (221) 33 514 20 48 <span class="sep">|</span> <span class="label">F</span>: (221) 33 514 20 49<br>
        <span class="label">E</span>: name@varnel.com <span class="sep">|</span> <span class="web">www.varnel.com</span>
      </p>
    </div>
    <div class="address-band">Rue des Palmiers - Bel Air, BP 210 - City, Country</div>
  </section>

  <section class="card card-back">
    <div class="brand"><span class="brand-dot"></span><span class="brand-name">Varnel Solutions</span></div>
    <p class="back-web">www.varnel.com</p>
    <div class="back-edge"></div>
  </section>
</main>
</body>
</html>
```